Business card for a business coach / management consultant

My logo has been done and now I need a business card. Deliverable needs to be a PDF to give to the printer. I want it single sided as I want the back side blank.
I prefer a white card with modern simple professional design.
Details are:
Tobias Wrenfield
B.Sc. (hons) FRTB CP MEGOL
14 Calloway Rd
Marlowe WA 6027
Australia
mobile 041 23 584 17
email tobias@corporatepathlane.com.au
skype tobiaswrenfield8
Small to medium size business owners
Business

```html
<!DOCTYPE html>
<html lang="en">
<head>
<meta charset="utf-8">
<title>Tobias Wrenfield – Business Card</title>
<link rel="stylesheet" href="https://fonts.googleapis.com/css2?family=Ubuntu:wght@400;500&display=swap">
<style>
  :root {
    --brand-blue: #29abe2;
    --ink: #111111;
    --paper: #ffffff;
  }
  * { margin: 0; padding: 0; box-sizing: border-box; }
  html, body {
    width: 1200px;
    height: 900px;
    overflow: hidden;
    background: var(--paper);
  }
  .card {
    position: relative;
    width: 1200px;
    height: 900px;
    background: var(--paper);
    font-family: "Ubuntu", sans-serif;
    color: var(--ink);
  }
  .band {
    position: absolute;
    left: 74px;
    width: 1050px;
    height: 56px;
    background: var(--brand-blue);
  }
  .band--top { top: 132px; }
  .band--bottom { top: 710px; }

  .identity {
    position: absolute;
    left: 144px;
    top: 340px;
    width: 400px;
    text-align: center;
  }
  .logo-placeholder {
    width: 116px;
    height: 116px;
    margin: 0 auto;
    border: 4px solid var(--brand-blue);
    border-radius: 6px;
    display: flex;
    align-items: center;
    justify-content: center;
    font-size: 25px;
    line-height: 1.25;
    color: var(--ink);
  }
  .person-name {
    margin-top: 40px;
    font-size: 47px;
    font-weight: 400;
    line-height: 1;
    letter-spacing: 0.3px;
  }
  .credentials {
    margin-top: 12px;
    font-size: 25px;
    color: var(--brand-blue);
    line-height: 1.2;
  }

  .divider {
    position: absolute;
    left: 590px;
    top: 352px;
    width: 4px;
    height: 232px;
    background: var(--brand-blue);
  }

  .address {
    position: absolute;
    left: 632px;
    top: 337px;
    font-style: normal;
    font-size: 26px;
    line-height: 36px;
  }

  .contact-list {
    position: absolute;
    left: 638px;
    top: 475px;
    list-style: none;
    font-size: 26px;
    line-height: 36px;
  }
  .contact-list li {
    display: flex;
    align-items: center;
    gap: 12px;
  }
  .contact-icon {
    width: 26px;
    height: 26px;
    flex: none;
  }
</style>
</head>
<body>
  <main class="card">
    <div class="band band--top"></div>

    <section class="identity">
      <div class="logo-placeholder">LOGO<br>HERE</div>
      <h1 class="person-name">Tobias Wrenfield</h1>
      <p class="credentials">B.Sc. (hons) FRTB CP MEGOL</p>
    </section>

    <div class="divider"></div>

    <address class="address">
      14 Calloway Rd<br>
      Marlowe WA 6027<br>
      Australia
    </address>

    <ul class="contact-list">
      <li>
        <svg class="contact-icon" viewBox="0 0 26 26" aria-label="Phone">
          <path d="M3 9 C3 5 7 4 13 4 C19 4 23 5 23 9 L23 11 L18 11 L17 8 L9 8 L8 11 L3 11 Z" fill="#111"/>
          <path d="M8 12 L18 12 L21 20 Q21 22 19 22 L7 22 Q5 22 5 20 Z" fill="#111"/>
          <circle cx="13" cy="17" r="2.6" fill="#fff"/>
        </svg>
        <span>041 23 584 17</span>
      </li>
      <li>
        <svg class="contact-icon" viewBox="0 0 26 26" aria-label="Email">
          <rect x="2.5" y="6" width="21" height="14" fill="none" stroke="#111" stroke-width="1.8"/>
          <path d="M3 6.8 L13 14 L23 6.8 M3 19.5 L10.5 12.5 M23 19.5 L15.5 12.5" fill="none" stroke="#111" stroke-width="1.6"/>
        </svg>
        <span>tobias@corporatepathlane.com.au</span>
      </li>
      <li>
        <svg class="contact-icon" viewBox="0 0 26 26" aria-label="Chat handle">
          <circle cx="13" cy="13" r="9" fill="#111"/>
        </svg>
        <span>tobiaswrenfield8</span>
      </li>
    </ul>

    <div class="band band--bottom"></div>
  </main>
</body>
</html>
```